Van Signage Wrapping

Hi there, my name is Wade; I have a business called "Brixol" servicing the Electrical, Security & AV (audio visual) industry. I currently have 2 X Vans working in Australia; I am looking to design a the graphics & lay out for the 2 X vans to be identical wrapped.
Should you wish to see the Van appearance (silver)
http://www.morvane.com.au/cars/plenvan/colours
http://www.morvane.com.au/cars/plenvan/home

Dimensions of the side panels are:
from the revision mirror to the tail 3.6meters
from the bottom if plastic to the top 1.35meters

Some of the words that describe our services are:
Commercial, Domestic, Automation, Networking, Data, Access Control, Alarms, CCTV, Audio Visual, Surround Sound, Home Cinema.
Allot of our work is taking these various technologies & linking them together for the user
Updates

Hi there, I have added a couple of thoughts in the 'nice to have' area of the brief I am very interested to see how you guys go, thank you for your designs so farĀ 

Target Market(s)

Builders, Developers, Home Owners, Buissness Owners

Industry/Entity Type

Plastic

Requirements
Must have
• The Logo "Brixol" which is attached to the project
(m)0412 574 306
(e)sales@brixol.com.au

I would like the side Logo on the van to run diagonal & hopefully take most of the advertising space over the sliding door & rear panel

REC No: 48302
Nice to have
• I have spent a little extra money on the Vans with more to come and I believe they look sharp & clean with the view to target well to do clients & larger projects, it would be great to keep the vans looking professional & clean. I like blue, white, black, lime-pale green against the silver colour but open to surjection.
In my head I imagined the Brixol logo running on the largest side panels on the diagonal with the Electrical, Security, AV also running the length underneath the logo. With some of the words mentioned above that describe our services in various shades randomly placed horizontally in the back ground linked together with a sort of printed circuit board pattern. Again I am very open to ideas so please feel free to get creative. You can see one image I have uploaded a picture of a Ute with some words that are randomly placed & similar to the shade I am thinking of, I also like the Lime/Pale Green on the Ute if you can make it work
Measurements of Van Panels are attached

```html
<!DOCTYPE html>
<html lang="en">
<head>
<meta charset="utf-8">
<title>Brixol – Van Signage</title>
<link rel="stylesheet" href="https://fonts.googleapis.com/css2?family=Arimo:wght@400;700&family=Archivo+Black&family=Cinzel:wght@400&display=swap">
<style>
  :root {
    --paper: #ffffff;
    --ink: #6b6560;
    --ink-dark: #58534f;
    --lime: #a3d284;
    --band: #c4cad4;
    --band-light: #d6dbe2;
    --word-light: #9ea4ad;
    --word-dark: #63605e;
    --silver-hi: #f2f3f4;
    --silver-lo: #b9bcc0;
  }
  * { margin: 0; padding: 0; box-sizing: border-box; }
  html, body { width: 1200px; height: 1000px; overflow: hidden; background: var(--paper); }
  .sheet { position: relative; width: 1200px; height: 1000px; font-family: "Arimo", Arial, sans-serif; }

  .brand { position: absolute; }
  .brand-name { font-family: "Arimo", Arial, sans-serif; font-weight: 400; line-height: 1; letter-spacing: 2px; }
  .brand-tag { font-family: "Cinzel", serif; font-size: 11px; letter-spacing: 0.5px; margin-top: 6px; margin-left: 48px; }

  .brand--plain { left: 74px; top: 70px; color: var(--ink); }
  .brand--plain .brand-name { font-size: 118px; }
  .brand--plain .brand-tag { color: var(--ink-dark); }

  .contact { position: absolute; color: var(--ink); }
  .contact-phone { font-family: "Archivo Black", Arial, sans-serif; font-size: 33px; letter-spacing: 1px; line-height: 1.05; }
  .contact-email { font-size: 27px; line-height: 1.1; }
  .contact--plain { left: 104px; top: 252px; }

  .panel { position: absolute; left: 477px; top: 68px; width: 646px; height: 188px; }
  .panel svg { position: absolute; inset: 0; }
  .contact--panel { left: 44px; top: 70px; color: var(--paper); }
  .contact--panel .contact-phone { font-size: 25px; }
  .contact--panel .contact-email { font-size: 19px; }
  .brand--panel { left: 300px; top: 22px; color: var(--paper); }
  .brand--panel .brand-name { font-size: 112px; }
  .brand--panel .brand-tag { color: var(--paper); }

  .van-photo {
    position: absolute; left: 172px; top: 330px; width: 908px; height: 420px;
    border-radius: 60px 140px 30px 30px;
    background: linear-gradient(180deg, var(--silver-hi) 0%, #dcdee0 55%, var(--silver-lo) 100%);
  }

  .word-band { position: absolute; left: 68px; top: 790px; width: 1058px; height: 162px; }
  .word-band svg { position: absolute; inset: 0; }
  .word { position: absolute; white-space: nowrap; transform: rotate(-6deg); transform-origin: left center; line-height: 1; font-weight: 700; }
  .word--light { color: var(--word-light); }
  .word--dark { color: var(--word-dark); }
  .word--regular { font-weight: 400; }
</style>
</head>
<body>
<main class="sheet">

  <div class="brand brand--plain">
    <div class="brand-name">Brixol</div>
    <div class="brand-tag">ELECTRICAL, SECURITY, AV</div>
  </div>

  <div class="contact contact--plain">
    <div class="contact-phone">0412 574 306</div>
    <div class="contact-email">sales@brixol.com.au</div>
  </div>

  <section class="panel">
    <svg width="646" height="188" viewBox="0 0 646 188" aria-hidden="true">
      <path d="M30 0 H616 Q646 0 646 30 V82 L542 188 H30 Q0 188 0 158 V30 Q0 0 30 0 Z" fill="var(--lime)"/>
    </svg>
    <div class="contact contact--panel">
      <div class="contact-phone">0412 574 306</div>
      <div class="contact-email">sales@brixol.com.au</div>
    </div>
    <div class="brand brand--panel">
      <div class="brand-name">Brixol</div>
      <div class="brand-tag">ELECTRICAL, SECURITY, AV</div>
    </div>
  </section>

  <div class="van-photo" role="img" aria-label="Silver panel van in side view wearing the Brixol wrap: green logo panel with contact details over the sliding door and a grey band of service words below"></div>

  <section class="word-band">
    <svg width="1058" height="162" viewBox="0 0 1058 162" aria-hidden="true">
      <path d="M0 18 H1058 V162 H0 Z" fill="var(--band)"/>
      <path d="M0 18 Q150 -10 330 20 Q380 32 360 85 Q335 150 420 162 H0 Z" fill="var(--band-light)"/>
    </svg>
    <span class="word word--dark word--regular" style="left:20px;top:34px;font-size:44px;">Home Cinema</span>
    <span class="word word--dark" style="left:335px;top:34px;font-size:31px;">Domestic</span>
    <span class="word word--light" style="left:402px;top:54px;font-size:42px;">Access Control</span>
    <span class="word word--dark" style="left:550px;top:80px;font-size:29px;">Automation</span>
    <span class="word word--dark word--regular" style="left:740px;top:39px;font-size:32px;">Networking</span>
    <span class="word word--light" style="left:922px;top:32px;font-size:19px;">Commercial</span>
    <span class="word word--dark" style="left:452px;top:108px;font-size:40px;">Data</span>
    <span class="word word--light" style="left:562px;top:112px;font-size:44px;">Surround Sound</span>
    <span class="word word--dark word--regular" style="left:922px;top:72px;font-size:36px;">Alarms</span>
    <span class="word word--dark" style="left:665px;top:140px;font-size:20px;">Audio Visual</span>
    <span class="word word--light" style="left:817px;top:124px;font-size:32px;">CCTV</span>
  </section>

</main>
</body>
</html>
```